Business Card Design

Sports massage therapist
Would like to convey a simple message.
graphic of human anatomy/muscular system
colours: orange with white/and or grey
glossey

Business

Fiona Tarrant
Soft Tissue Therapist
Sports and Remedial Massage
07914 562038
tarrant.fiona@pelmora.co.uk

```html
<!DOCTYPE html>
<html lang="en">
<head>
<meta charset="utf-8">
<title>Fiona Tarrant – Soft Tissue Therapist</title>
<link href="https://fonts.googleapis.com/css2?family=Source+Sans+3:ital,wght@0,400;0,700;1,400&display=swap" rel="stylesheet">
<style>
  :root {
    --orange: #f5570f;
    --orange-light: #f47c3c;
    --slate: #59656d;
    --grey-text: #6b7275;
    --ink: #111111;
    --paper: #ffffff;
    --muscle: #c65a4a;
    --muscle-pale: #efd3c8;
  }
  html, body {
    margin: 0;
    padding: 0;
    width: 1200px;
    height: 791px;
    overflow: hidden;
    background: var(--paper);
  }
  .card {
    position: relative;
    width: 1200px;
    height: 791px;
    background: var(--paper);
    font-family: "Source Sans 3", "Source Sans Pro", Arial, sans-serif;
    overflow: hidden;
  }
  .anatomy-figure {
    position: absolute;
    left: 0;
    top: 0;
    width: 580px;
    height: 716px;
    background:
      radial-gradient(ellipse 40% 48% at 48% 45%, var(--muscle) 0%, rgba(198,90,74,0.75) 45%, rgba(239,211,200,0.5) 75%, rgba(255,255,255,0) 100%),
      radial-gradient(ellipse 30% 45% at 12% 40%, var(--muscle-pale) 0%, rgba(255,255,255,0) 100%);
  }
  .identity {
    position: absolute;
    right: 80px;
    top: 78px;
    text-align: right;
  }
  .identity__name {
    margin: 0;
    font-size: 47px;
    font-weight: 700;
    color: var(--orange-light);
    line-height: 1;
    letter-spacing: 0.3px;
  }
  .identity__role {
    margin: 18px 0 0;
    font-size: 32px;
    font-style: italic;
    color: var(--grey-text);
    line-height: 1;
  }
  .identity__service {
    margin: 16px 0 0;
    font-size: 32px;
    color: var(--ink);
    line-height: 1;
  }
  .contact-list {
    position: absolute;
    right: 174px;
    top: 474px;
    margin: 0;
    padding: 0;
    list-style: none;
    text-align: right;
  }
  .contact-list li {
    font-size: 35px;
    font-weight: 700;
    color: var(--grey-text);
    line-height: 1;
    margin-bottom: 35px;
  }
  .contact-tab {
    position: absolute;
    left: 1065px;
    top: 443px;
    width: 135px;
    height: 170px;
    background: var(--orange);
    border-radius: 24px 0 0 24px;
  }
  .contact-tab svg {
    position: absolute;
    left: 32px;
  }
  .contact-tab .icon-phone { top: 28px; }
  .contact-tab .icon-mail { top: 104px; }
  .footer-bands {
    position: absolute;
    left: 0;
    bottom: 0;
  }
</style>
</head>
<body>
<div class="card">
  <div class="anatomy-figure" role="img" aria-label="Illustration of a running human figure showing the muscular system and skeleton"></div>

  <header class="identity">
    <h1 class="identity__name">Fiona Tarrant</h1>
    <p class="identity__role">Soft Tissue Therapist</p>
    <p class="identity__service">Sports and Remedial Massage</p>
  </header>

  <ul class="contact-list">
    <li>07914 562038</li>
    <li>tarrant.fiona@pelmora.co.uk</li>
  </ul>

  <div class="contact-tab">
    <svg class="icon-phone" width="44" height="40" viewBox="0 0 44 40" aria-hidden="true">
      <path d="M4 12 C4 4 40 4 40 12 L40 16 L31 16 L31 11 C26 9 18 9 13 11 L13 16 L4 16 Z" fill="#fff"/>
      <path d="M12 18 L32 18 L38 36 L6 36 Z" fill="#fff"/>
      <g fill="var(--orange)">
        <rect x="16" y="22" width="3" height="3"/><rect x="21" y="22" width="3" height="3"/><rect x="26" y="22" width="3" height="3"/>
        <rect x="15" y="27" width="3" height="3"/><rect x="21" y="27" width="3" height="3"/><rect x="27" y="27" width="3" height="3"/>
      </g>
    </svg>
    <svg class="icon-mail" width="42" height="32" viewBox="0 0 42 32" aria-hidden="true">
      <rect x="1.5" y="1.5" width="39" height="29" fill="none" stroke="#fff" stroke-width="3"/>
      <path d="M2 3 L21 19 L40 3 M2 29 L16 15 M40 29 L26 15" fill="none" stroke="#fff" stroke-width="3"/>
    </svg>
  </div>

  <svg class="footer-bands" width="1200" height="80" viewBox="0 0 1200 80" aria-hidden="true">
    <path d="M0 5 L700 5 C680 20 668 50 660 80 L0 80 Z" fill="var(--slate)"/>
    <path d="M650 80 C670 40 700 2 770 2 L1200 2 L1200 80 Z" fill="var(--orange)" stroke="#fff" stroke-width="6"/>
  </svg>
</div>
</body>
</html>
```